Corvane Supplies Business Card

Professional business card that stand out to our potential customers. Front and back with clean modern design

Industry/Entity Type

Oil and gas

Contact Information for Business Card

Name, address, website , office phone and cell number

Requirements
Must have
• Editable files for each employee

```html
<!DOCTYPE html>
<html lang="en">
<head>
<meta charset="utf-8">
<title>Corvane Supplies Business Card</title>
<link rel="stylesheet" href="https://fonts.googleapis.com/css2?family=Poppins:wght@400;500;700&display=swap">
<style>
  :root {
    --backdrop: #7598c6;
    --card: #ffffff;
    --map-tone: #ececec;
    --brand-red: #f20c0c;
    --brand-cyan: #10aed0;
    --ink: #1d1d1d;
    --ink-soft: #444444;
  }
  * { box-sizing: border-box; margin: 0; padding: 0; }
  html, body {
    width: 1200px; height: 912px; overflow: hidden;
    background: var(--backdrop);
    font-family: "Poppins", sans-serif;
  }
  .sheet {
    position: relative; width: 1200px; height: 912px;
    display: flex; gap: 40px; align-items: center; justify-content: center;
  }
  .card {
    position: relative; width: 540px; height: 309px;
    background: var(--card); overflow: hidden;
    box-shadow: 0 10px 26px rgba(20, 40, 80, 0.28);
  }
  .map-backdrop {
    position: absolute; left: 40px; top: 24px; width: 460px; height: 230px;
    background: radial-gradient(ellipse at center, var(--map-tone) 0%, rgba(236,236,236,0.6) 55%, rgba(255,255,255,0) 75%);
  }
  .red-band {
    position: absolute; left: 0; right: 0; bottom: 0; height: 34px;
    background: var(--brand-red);
  }
  .brand {
    position: absolute; display: flex; align-items: center; gap: 10px;
  }
  .brand-mark {
    width: 22px; height: 22px; background: var(--brand-cyan);
  }
  .brand-name {
    font-weight: 700; color: var(--brand-red); text-transform: uppercase;
    letter-spacing: 0.5px; white-space: nowrap;
  }
  .card-front .brand { left: 50%; top: 128px; transform: translateX(-50%); }
  .card-front .brand-name { font-size: 30px; }
  .card-front .brand-mark { width: 28px; height: 28px; }

  .card-back .brand { left: 28px; top: 140px; }
  .card-back .brand-name { font-size: 19px; }

  .person { position: absolute; left: 270px; top: 30px; }
  .person-name { font-size: 30px; font-weight: 700; color: var(--ink); line-height: 1.05; }
  .person-role { font-size: 11px; font-weight: 500; color: var(--ink-soft); margin-left: 2px; }

  .contact-rail {
    position: absolute; left: 252px; top: 106px; width: 34px; height: 150px;
    background: var(--brand-cyan); border-radius: 10px;
    display: flex; flex-direction: column; align-items: center; justify-content: space-around;
    padding: 8px 0;
  }
  .contact-rail svg { width: 15px; height: 15px; fill: #ffffff; }
  .contact-list {
    position: absolute; left: 300px; top: 137px; list-style: none;
    font-size: 14px; color: var(--ink); line-height: 30px;
  }
  .address {
    position: absolute; left: 0; right: 0; bottom: 0; height: 34px;
    display: flex; align-items: center; justify-content: center; gap: 8px;
    color: #ffffff; font-size: 13px; font-weight: 500;
  }
  .address svg { width: 12px; height: 14px; fill: #ffffff; }
</style>
</head>
<body>
<main class="sheet">
  <section class="card card-front" aria-label="Card front">
    <div class="map-backdrop" role="img" aria-label="Faint grey world map backdrop"></div>
    <div class="brand">
      <span class="brand-mark"></span>
      <span class="brand-name">Corvane Supplies</span>
    </div>
    <div class="red-band"></div>
  </section>

  <section class="card card-back" aria-label="Card back">
    <div class="map-backdrop" role="img" aria-label="Faint grey world map backdrop"></div>
    <div class="brand">
      <span class="brand-mark"></span>
      <span class="brand-name">Corvane Supplies</span>
    </div>

    <div class="person">
      <h1 class="person-name">Dana Whitlock</h1>
      <p class="person-role">senior engineer</p>
    </div>

    <div class="contact-rail">
      <svg viewBox="0 0 16 16" aria-hidden="true"><circle cx="8" cy="5" r="3.2"/><path d="M2 15c0-3.6 2.7-5.6 6-5.6s6 2 6 5.6z"/></svg>
      <svg viewBox="0 0 16 16" aria-hidden="true"><path d="M4 1.5l2.2 3-1.3 1.6c.9 2 2.4 3.6 4.4 4.6l1.6-1.3 3 2.2-1.2 2.4C7.6 14 2 8.4 1.5 3z"/></svg>
      <svg viewBox="0 0 16 16" aria-hidden="true"><path d="M1 3.5h14v9H1z M1.5 4l6.5 5 6.5-5" stroke="#10aed0" stroke-width="1"/></svg>
      <svg viewBox="0 0 16 16" aria-hidden="true"><circle cx="8" cy="8" r="6.5"/><path d="M1.5 8h13M8 1.5c-2.5 3-2.5 10 0 13M8 1.5c2.5 3 2.5 10 0 13" stroke="#10aed0" stroke-width="1" fill="none"/></svg>
    </div>
    <ul class="contact-list">
      <li>(555)014-0276</li>
      <li>sales@corvanesupplies.com</li>
      <li>www.corvanesupplies.com</li>
    </ul>

    <div class="red-band"></div>
    <p class="address">
      <svg viewBox="0 0 12 14" aria-hidden="true"><path d="M6 0a5 5 0 0 0-5 5c0 3.6 5 9 5 9s5-5.4 5-9a5 5 0 0 0-5-5zm0 7a2 2 0 1 1 0-4 2 2 0 0 1 0 4z"/></svg>
      418 N.Ridgeline Suite 5 Midland, Tx 79701
    </p>
  </section>
</main>
</body>
</html>
```